Custom Business Card Design

We are looking for a raised spot logo design to use with Trellu.com. We will provide the logo files. Should be a front and back design. We want to implement the house into the back design using the same colors as the logo through out. Something VERY cool!

```html
<!DOCTYPE html>
<html lang="en">
<head>
<meta charset="utf-8">
<title>Pellora Business Card – Front and Back</title>
<link rel="stylesheet" href="https://fonts.googleapis.com/css2?family=Source+Sans+3:wght@400;600&display=swap">
<style>
  :root {
    --stage: #000000;
    --card: #2f3034;
    --card-edge: #35363a;
    --brand-blue: #2b78be;
    --text-grey: #b4b4b6;
    --divider: #4a4b4f;
  }
  * { margin: 0; padding: 0; box-sizing: border-box; }
  html, body {
    width: 1200px; height: 900px; overflow: hidden;
    background: var(--stage);
    font-family: "Source Sans 3", "Myriad Pro", Arial, sans-serif;
  }
  .stage { position: relative; width: 1200px; height: 900px; }
  .card {
    position: absolute; top: 271px;
    width: 457px; height: 281px;
    border-radius: 13px;
    background: linear-gradient(180deg, var(--card-edge), var(--card));
  }
  .card-front { left: 137px; }
  .card-back { left: 626px; }

  .front-brand {
    position: absolute; left: 30px; top: 120px; width: 190px;
    display: flex; align-items: center; justify-content: center; gap: 10px;
  }
  .brand-dot {
    width: 30px; height: 30px; border-radius: 50%;
    background: var(--brand-blue); flex: none;
  }
  .brand-name {
    color: var(--brand-blue); font-weight: 600; line-height: 1;
  }
  .front-brand .brand-name { font-size: 38px; }

  .divider {
    position: absolute; left: 236px; top: 66px;
    width: 1px; height: 150px; background: var(--divider);
  }
  .contact { position: absolute; left: 262px; top: 67px; color: var(--text-grey); }
  .person-name {
    color: var(--brand-blue); font-size: 20.5px; font-weight: 600;
    letter-spacing: 0.2px; line-height: 22px;
  }
  .person-role { font-size: 13.5px; line-height: 16px; }
  .address { margin-top: 9px; font-size: 13.5px; line-height: 17px; }
  .lines { margin-top: 8px; list-style: none; font-size: 13.5px; line-height: 16.5px; }
  .lines li { display: flex; align-items: center; gap: 6px; }
  .lines svg { width: 11px; height: 11px; fill: var(--brand-blue); flex: none; }

  .back-brand {
    position: absolute; left: 0; right: 0; top: 118px;
    display: flex; align-items: center; justify-content: center; gap: 12px;
  }
  .back-brand .brand-name { font-size: 42px; }
  .website {
    position: absolute; left: 0; right: 0; top: 212px;
    text-align: center; color: var(--text-grey); font-size: 13.5px;
  }
</style>
</head>
<body>
<main class="stage">
  <section class="card card-front" aria-label="Card front">
    <div class="front-brand">
      <span class="brand-dot"></span>
      <span class="brand-name">Pellora</span>
    </div>
    <div class="divider"></div>
    <div class="contact">
      <p class="person-name">JONATHAN SMITH</p>
      <p class="person-role">Managing Director</p>
      <p class="address">12345, Address Goes Here<br>Country Name, 123456.</p>
      <ul class="lines">
        <li><svg viewBox="0 0 12 12" aria-hidden="true"><path d="M1 4c0-2 2-3 5-3s5 1 5 3l-2 1-1-1.5H4L3 5zM3 6h6l1.5 5h-9z"/></svg>044-123 456 789</li>
        <li><svg viewBox="0 0 12 12" aria-hidden="true"><path d="M3.5 0h5a1 1 0 0 1 1 1v10a1 1 0 0 1-1 1h-5a1 1 0 0 1-1-1V1a1 1 0 0 1 1-1zm.5 1.5v7.5h4V1.5z"/></svg>044-123 456 789</li>
        <li><svg viewBox="0 0 12 12" aria-hidden="true"><path d="M0 2.5h12v7H0zM1 3.3l5 3.5 5-3.5v-.3H1z"/></svg>info@webname.com</li>
      </ul>
    </div>
  </section>

  <section class="card card-back" aria-label="Card back">
    <div class="back-brand">
      <span class="brand-dot"></span>
      <span class="brand-name">Pellora</span>
    </div>
    <p class="website">www.websitename.com</p>
  </section>
</main>
</body>
</html>
```